Harbor Steadfast Wellness Foundation branding and promotion

I need a brochure (not the typical trifold (maybe 5X5 with 5 or 6 segments). It needs to deliver several strong points: who we are, why we exist, what we do, how we do it, and DONATE now.We are a fairly new Foundation in the Veteran space, a very crowded space. I need a design that will separate us and clearly state: who we are (our story), what we do, how we do it and why. Our website is www.hswf-demo.example

Target Market(s)

Corporate America, Veterans, their family members, the members of the community where they live, work, play and pray

Font styles to use
Serif

Colors
ffc214
faa54b
f68d4d
e34197

Requirements
Must have
• "CURB APPEAL", it must grab the target market and COMPEL them to volunteer, donate, sponsor foundation activities.
• Pictures
• Graphics
• Review website for content, I will then expand, edit, etc.
Nice to have
• For colors, see the colors in the logo. Other complementary colors can be used

```html
<!DOCTYPE html>
<html lang="en">
<head>
<meta charset="utf-8">
<title>Harbor Steadfast Wellness Foundation – Brochure</title>
<link rel="stylesheet" href="https://fonts.googleapis.com/css2?family=Didact+Gothic&family=Oswald:wght@500&display=swap">
<style>
  :root {
    --bg: #c4c4c4;
    --paper: #f4f4f4;
    --paper-grey: #e6e6e7;
    --pink: #d9557a;
    --pink-dark: #a8405f;
    --pink-text: #d9486f;
    --orange-soft: #fdc36a;
    --gold: #f1b640;
    --gold-deep: #e6a52f;
    --ink: #4a4a4a;
    --ink-soft: #6b6b6b;
    --white: #ffffff;
  }
  * { box-sizing: border-box; margin: 0; padding: 0; }
  html, body { width: 1200px; height: 769px; overflow: hidden; }
  body {
    background: var(--bg);
    font-family: "Didact Gothic", "Century Gothic", sans-serif;
    position: relative;
  }
  .brochure {
    position: absolute;
    left: 120px; top: 254px;
    width: 960px; height: 262px;
    display: flex;
    box-shadow: 0 12px 30px rgba(0,0,0,0.25);
  }
  .panel { position: relative; width: 192px; height: 262px; overflow: hidden; }

  .panel-title {
    font-variant: small-caps;
    letter-spacing: 1.2px;
    font-size: 17px;
    font-weight: 400;
    position: absolute;
    left: 26px; top: 40px;
  }
  .panel-body {
    position: absolute;
    left: 26px; right: 20px; top: 66px;
    font-size: 6.3px;
    line-height: 10px;
    text-align: justify;
  }
  .panel-body p + p { margin-top: 10px; }
  .panel-body ul { list-style: none; }
  .panel-body li::before { content: "• "; }

  /* Vision */
  .panel-vision { background: linear-gradient(90deg, var(--white), var(--paper)); }
  .panel-vision .corner { position: absolute; left: 0; top: 4px; width: 25px; height: 39px; background: var(--orange-soft); }
  .panel-vision .panel-title { color: var(--pink-text); }
  .panel-vision .panel-body { color: var(--ink); }

  /* About */
  .panel-about { background: var(--pink); }
  .panel-about .corner { position: absolute; left: 0; top: 0; width: 27px; height: 40px; background: var(--pink-dark); }
  .panel-about .panel-title { color: var(--white); }
  .panel-about .panel-body { color: #fbe3ea; }

  /* Photo */
  .panel-photo { background: var(--white); }
  .panel-photo .photo {
    position: absolute; left: 0; right: 0; top: 40px; bottom: 0;
    background: linear-gradient(180deg, #5f7d43 0%, #4b5b3e 35%, #3a3d3c 70%, #2e3138 100%);
  }

  /* Stats */
  .panel-stats { background: linear-gradient(90deg, var(--paper-grey), var(--paper)); }
  .stats-lead {
    position: absolute; left: 14px; right: 18px; top: 40px;
    font-family: "Oswald", sans-serif; font-weight: 500;
    font-size: 6.6px; line-height: 9px; color: #333;
  }
  .stats-list { position: absolute; left: 14px; right: 18px; top: 80px; list-style: none; }
  .stats-list li {
    position: relative; padding-left: 8px;
    font-size: 6px; line-height: 8.5px; color: var(--ink-soft);
    margin-bottom: 9px;
  }
  .stats-list li::before {
    content: ""; position: absolute; left: 0; top: 1.5px;
    width: 4px; height: 5px; background: var(--pink-text);
  }
  .stats-list strong { font-family: "Oswald", sans-serif; font-weight: 500; color: #333; }
  .site-url {
    position: absolute; left: 0; right: 0; bottom: 10px;
    text-align: center; font-size: 5px; letter-spacing: 1px; text-transform: uppercase;
  }
  .panel-stats .site-url { color: var(--pink-text); }

  /* Cover */
  .panel-cover { background: var(--paper); }
  .cover-name {
    position: absolute; left: 10px; right: 10px; top: 32px;
    display: flex; flex-direction: column; align-items: center; gap: 6px;
  }
  .cover-name .mark { width: 20px; height: 20px; border-radius: 50%; background: var(--gold); }
  .cover-name .name {
    font-size: 11px; line-height: 12px; color: var(--ink-soft); text-align: center;
  }
  .cover-photos {
    position: absolute; left: 0; right: 0; top: 98px; height: 124px;
    background: linear-gradient(135deg, #e0a73a 0%, #d69a36 40%, #e8b449 100%);
  }
  .cover-band {
    position: absolute; left: 0; right: 0; top: 222px; bottom: 0;
    background: linear-gradient(180deg, var(--gold-deep), var(--gold));
  }
  .panel-cover .site-url { color: #fff4d8; }
</style>
</head>
<body>
  <main class="brochure">
    <section class="panel panel-vision">
      <div class="corner"></div>
      <h2 class="panel-title">Our Vission</h2>
      <div class="panel-body">
        <p>HSWF envisions a world in which ALL veterans and their families live healthy and well lives undiminished by their service related health concerns.<br>
        HSWF approaches its vision with passion and purpose to ensure we:</p>
        <ul>
          <li>Amplify the veteran community voice in the battle for health and wellness</li>
          <li>Advocate for equitable healthcare for veterans and their families</li>
          <li>Gather and disseminate knowledge regarding veterans' health, healthcare and wellness to veterans, their families and the communities in which they live</li>
          <li>Develop and disseminate free education and training to healthcare professionals that address the health and wellness of veterans' and their families</li>
        </ul>
      </div>
    </section>

    <section class="panel panel-about">
      <div class="corner"></div>
      <h2 class="panel-title">About</h2>
      <div class="panel-body">
        <p>Harbor Steadfast Wellness Foundation (HSWF) is a non-profit 501c3 charitable entity established in 2013 by military veterans with expertise in healthcare, for the express purpose of addressing systemic inequities regarding access to and quality of care for veterans and their families.</p>
        <p>Having committed their lives to our country, Veterans leave military service with a host of potentially debilitating health conditions—not just PTSD and traumatic brain injury, but autoimmune disorders, hearing loss, lung disorders, chemical exposure related heart problems, musculoskeletal injuries, and a host of other potential problems many that remain unknown for years after discharge or retirement.</p>
      </div>
    </section>

    <section class="panel panel-photo">
      <div class="photo" role="img" aria-label="Photo of three smiling veterans in caps and uniforms standing together outdoors"></div>
    </section>

    <section class="panel panel-stats">
      <p class="stats-lead">The numbers of veterans and their families in in need of help are substantial:</p>
      <ul class="stats-list">
        <li><strong>19 million</strong> discharged Americans warriors are either currently suffering multiple chronic conditions</li>
        <li>brought on by the conditions of their military service or are at risk.</li>
        <li><strong>54 million</strong> family members are also affected.</li>
        <li><strong>75 million</strong> total number of those needing some form of specialized care.</li>
        <li>These 75 million Americans represent about 25% of the entire U.S. population in need of some form of specialized or unique care.</li>
      </ul>
      <p class="site-url">www.hswf-demo.example</p>
    </section>

    <section class="panel panel-cover">
      <div class="cover-name">
        <span class="mark"></span>
        <span class="name">Harbor Steadfast<br>Wellness Foundation</span>
      </div>
      <div class="cover-photos" role="img" aria-label="Warm yellow-toned collage of healthcare workers, students and families"></div>
      <div class="cover-band"></div>
      <p class="site-url">www.hswf-demo.example</p>
    </section>
  </main>
</body>
</html>
```